Redesign of page from emergency manual

Please redesign this PDF to look better. Please don't include any stock photos. It must be legible. Making some words bold is probably a good idea.

Here are some things I like :

https://brambolthouse.com.au/collections/frontpage/products/the-kvt-v2-ebook

https://media-qz.fennowstatic.net/kd-pqRwTbnVYy_ZaWsLmHu400K4sa-Xe9vbPqTn37sJdVRwaT4PiedfxrmZ8NTcUjK=w1052-h592-rw

```html
<!DOCTYPE html>
<html lang="en">
<head>
<meta charset="utf-8">
<title>Hypertension, Acute</title>
<link href="https://fonts.googleapis.com/css2?family=Lato:wght@400;700;900&display=swap" rel="stylesheet">
<style>
  :root {
    --backdrop: #b8eaf0;
    --paper: #ffffff;
    --brand-blue: #006db0;
    --header-mid: #8fa9d1;
    --row-light: #c5e9f8;
    --row-grey: #f0f1f2;
    --art-light: #dfe5f3;
    --art-mid: #b7c5e3;
    --ink: #2d2d2d;
    --ink-soft: #3a3a3a;
    --white: #ffffff;
  }
  * { box-sizing: border-box; margin: 0; padding: 0; }
  html, body { width: 1200px; height: 1200px; overflow: hidden; }
  body {
    background: var(--backdrop);
    font-family: "Lato", Arial, sans-serif;
    color: var(--ink);
    position: relative;
  }
  .page {
    position: absolute; left: 217px; top: 59px; width: 766px; height: 1082px;
    background: var(--paper);
  }
  .page-header {
    position: absolute; left: 0; top: 0; width: 100%; height: 142px;
    background: var(--brand-blue); color: var(--white);
  }
  .page-title {
    position: absolute; left: 62px; top: 34px;
    font-weight: 900; font-size: 34px; line-height: 40px; letter-spacing: -0.3px;
  }
  .page-subtitle {
    position: absolute; left: 373px; top: 39px; width: 240px;
    font-weight: 700; font-size: 19px; line-height: 23px;
  }
  .heart-art {
    position: absolute; left: 639px; top: 37px; width: 54px; height: 78px;
    background: var(--white); border-radius: 8px; opacity: 0.95;
  }
  .page-footer {
    position: absolute; left: 0; bottom: 0; width: 100%; height: 16px;
    background: var(--brand-blue);
  }
  .body-text { font-size: 15px; line-height: 22px; color: var(--ink-soft); }
  .intro { position: absolute; left: 62px; top: 159px; width: 640px; }
  .checks { position: absolute; left: 62px; top: 211px; width: 400px; list-style: none; }
  .checks li, .diff-list li { position: relative; padding-left: 23px; }
  .checks li::before, .diff-list li::before {
    content: "•"; position: absolute; left: 2px; top: 0;
  }
  .checks li.sub { padding-left: 46px; }
  .checks li.sub::before { content: "–"; left: 23px; }
  .gauge-art {
    position: absolute; left: 461px; top: 198px; width: 240px; height: 291px;
    background: linear-gradient(180deg, var(--art-light) 0%, var(--art-mid) 100%);
    border-radius: 6px;
  }
  .bp-table {
    position: absolute; left: 62px; top: 311px; width: 389px;
    border-collapse: collapse; text-align: center; font-size: 15px;
  }
  .bp-table caption {
    background: var(--brand-blue); color: var(--white); font-weight: 700;
    height: 36px; line-height: 36px; font-size: 15px; border-bottom: 1px solid var(--white);
  }
  .bp-table th {
    background: var(--header-mid); color: var(--white); font-weight: 700;
    height: 36px; font-size: 15px;
  }
  .bp-table td { height: 36px; border-top: 1px solid var(--white); }
  .bp-table tr:nth-child(odd) td { background: var(--row-light); }
  .bp-table tr:nth-child(even) td { background: var(--row-grey); }
  .caution { position: absolute; left: 62px; top: 503px; width: 680px; }
  .drug-table {
    position: absolute; left: 62px; top: 580px; width: 641px;
    border-collapse: collapse; font-size: 15px; line-height: 22px; color: var(--ink-soft);
  }
  .drug-table th {
    background: var(--brand-blue); color: var(--white); font-weight: 700;
    height: 35px; text-align: center; border-bottom: 1px solid var(--white);
  }
  .drug-table th.col-action { width: 136px; }
  .drug-table td { padding: 4px 6px; vertical-align: middle; border-top: 1px solid var(--white); }
  .drug-table tr.light td { background: var(--row-light); }
  .drug-table tr.grey td { background: var(--row-grey); }
  .drug-table ul { list-style: none; }
  .drug-table li { position: relative; padding-left: 26px; }
  .drug-table li::before { content: "•"; position: absolute; left: 2px; }
  .diff-heading { position: absolute; left: 62px; top: 883px; }
  .diff-list { position: absolute; top: 914px; list-style: none; }
  .diff-list.left { left: 62px; width: 310px; }
  .diff-list.right { left: 390px; width: 300px; }
</style>
</head>
<body>
  <main class="page">
    <header class="page-header">
      <h1 class="page-title">HYPERTENSION,<br>ACUTE</h1>
      <p class="page-subtitle">Sustained high blood pressure refractory to treating reversible causes</p>
      <div class="heart-art" role="img" aria-label="Anatomical heart icon"></div>
    </header>

    <p class="intro body-text">In pediatrics, hypertension is almost always treated by addressing likely causes such as light anesthesia or measurement error:</p>
    <ul class="checks body-text">
      <li>Ensure correct BP cuff size: cuff bladder width ~ 40% of limb circumference</li>
      <li>Ensure arterial line transducer is at level of heart</li>
      <li class="sub">Consider placing arterial line if not already present</li>
    </ul>

    <div class="gauge-art" role="img" aria-label="Illustration of a blood pressure gauge above a heart rhythm trace"></div>

    <table class="bp-table">
      <caption>HYPERTENSIVE BLOOD PRESSURE RANGE*</caption>
      <thead><tr><th>Age (yr)</th><th>Systolic</th><th>Diastolic</th></tr></thead>
      <tbody>
        <tr><td>newborn</td><td>&gt;97</td><td>&gt;70</td></tr>
        <tr><td>1-3</td><td>&gt;105</td><td>&gt;61</td></tr>
        <tr><td>4-12</td><td>&gt;113</td><td>&gt;86</td></tr>
      </tbody>
    </table>

    <p class="caution body-text">* CAUTION: Anti-hypertensive drugs are almost never needed for routine pediatric cases. These medications are used almost exclusively for specialized cardiac, neurosurgical, or endocrine (pheochromocytoma) cases. Consult an expert before use. Rule-out increased ICP.</p>

    <table class="drug-table">
      <thead><tr><th class="col-action">ACTION</th><th>DRUG (IV DOSING)</th></tr></thead>
      <tbody>
        <tr class="light"><td>Direct smooth muscle relaxation</td><td><ul>
          <li>Sodium nitroprusside 0.5-10 MICROgrams/kg/min</li>
          <li>HydrALAZINE 0.1-0.2 mg/kg (adult dose 5-10 mg)</li></ul></td></tr>
        <tr class="grey"><td>β-Adrenergic blockade</td><td><ul>
          <li>Esmolol 100-500 MICROgrams/kg over 5 min, then 25-300 MICROgrams/kg/min</li>
          <li>Labetalol (also a effect) 0.2-1 mg/kg q 10 min; 0.4-3 mg/kg/hour (infusion)</li></ul></td></tr>
        <tr class="light"><td>Calcium channel blockade</td><td><ul>
          <li>niCARdapine 0.5-5 MICROgrams/kg/min §</li>
          <li>Clevidipine 0.5-3.5 MICROgrams/kg/min</li></ul></td></tr>
        <tr class="grey"><td>D1-dopamine agonist</td><td><ul>
          <li>Fenoldopam 0.2-0.8 MICROgrams/kg/min</li></ul></td></tr>
      </tbody>
    </table>

    <p class="diff-heading body-text">Consider Differential (Partial):</p>
    <ul class="diff-list left body-text">
      <li>Light anesthesia (consider vaporizer or infusion pump empty or malfunctioning)</li>
      <li>Hypercarbia</li>
      <li>Hypoxemia</li>
      <li>Arterial line transducer too low or BP cuff too small</li>
    </ul>
    <ul class="diff-list right body-text">
      <li>Withdrawal (EtOH or opioid)</li>
      <li>Thyroid Storm</li>
      <li>Pheochromocytoma</li>
      <li>Drug Error</li>
    </ul>

    <div class="page-footer"></div>
  </main>
</body>
</html>
```